Healthy Supplement featuring Moringa products

Need 3 business card options for our reps to order from Cardloom. Our reps will be ordering from Cardloom once we upload them. Attached is our current designs to show what info needs to be on the cards. Our website is www.tkvitality.com
The business cards will be a template for our reps to order from. Most of our reps are Asian & Hispanic. Please look at our website so you can see who we are to get the look and feel what we need.
Target Market(s)
Adults 30 on up. Health oriented people.
Industry/Entity Type
Health And Wellness
Contact Information for Business Card
Name
Title
Phone
Logo
www.tkvitality.com/my/username
Font styles to use
Requirements
Must have
- Please match our website look and colors. A moringa leaf is nice, but am open to something different.
Nice to have
- Healthy looking and warm, not super cold or too modern.
Should not have
- No harsh colors please.

```html
<!DOCTYPE html>
<html lang="en">
<head>
<meta charset="utf-8">
<title>TK Vitality – Business Card</title>
<link rel="stylesheet" href="https://fonts.googleapis.com/css2?family=Roboto:wght@400;700&display=swap">
<style>
  :root {
    --stage: #e6e7e9;
    --leaf-green: #6aaa44;
    --bright-green: #8dc63f;
    --charcoal: #323132;
    --orange: #f47920;
    --white: #ffffff;
    --body-text: #f2f2f2;
  }
  * { box-sizing: border-box; margin: 0; padding: 0; }
  html, body {
    width: 1200px; height: 800px; overflow: hidden;
    background: var(--stage);
    font-family: "Roboto", Arial, sans-serif;
  }
  .stage { position: relative; width: 1200px; height: 800px; }

  .card {
    position: absolute; width: 560px; height: 320px;
    box-shadow: 0 6px 18px rgba(0,0,0,0.18);
    overflow: hidden;
  }

  /* Front */
  .card-front {
    left: 580px; top: 70px;
    background: var(--leaf-green);
    display: flex; align-items: center; justify-content: center;
  }
  .brand { display: flex; align-items: center; gap: 14px; }
  .brand-dot { width: 26px; height: 26px; border-radius: 50%; }
  .card-front .brand-dot { background: var(--white); }
  .card-front .brand-name {
    color: var(--white); font-weight: 700; font-size: 46px; letter-spacing: 1px;
  }

  /* Back */
  .card-back {
    left: 60px; top: 410px;
    background: var(--charcoal);
  }
  .back-art { position: absolute; left: 0; top: 0; width: 230px; height: 320px; }
  .back-info {
    position: absolute; right: 36px; top: 40px;
    display: flex; flex-direction: column; align-items: flex-end; text-align: right;
  }
  .card-back .brand-dot { background: var(--bright-green); width: 20px; height: 20px; }
  .card-back .brand-name {
    color: var(--bright-green); font-weight: 700; font-size: 34px;
  }
  .rep-name {
    margin-top: 34px; color: var(--bright-green);
    font-weight: 700; font-size: 24px;
  }
  .rep-title { color: var(--orange); font-size: 17px; margin-top: 2px; }
  .contact-list { list-style: none; margin-top: 20px; }
  .contact-list li {
    display: flex; align-items: center; justify-content: flex-end; gap: 8px;
    color: var(--body-text); font-size: 17px; line-height: 24px;
  }
  .contact-icon { width: 15px; height: 15px; flex: none; }
</style>
</head>
<body>
<main class="stage">

  <section class="card card-front" aria-label="Business card front">
    <div class="brand">
      <span class="brand-dot"></span>
      <span class="brand-name">TK Vitality</span>
    </div>
  </section>

  <section class="card card-back" aria-label="Business card back">
    <svg class="back-art" viewBox="0 0 230 320" aria-hidden="false">
      <polygon points="0,0 170,0 0,290" fill="var(--orange)"/>
      <rect x="20" y="20" width="200" height="260" rx="60" fill="var(--bright-green)" opacity="0.85"
            transform="rotate(30 120 150)" role="img" aria-label="Moringa leaf branch illustration"/>
      <path d="M0,290 Q90,220 230,20 L236,26 Q110,240 0,305 Z" fill="var(--bright-green)"/>
    </svg>

    <div class="back-info">
      <div class="brand">
        <span class="brand-dot"></span>
        <span class="brand-name">TK Vitality</span>
      </div>
      <p class="rep-name">Daniel Reyes</p>
      <p class="rep-title">Representative</p>
      <ul class="contact-list">
        <li>(555) 014-2298
          <svg class="contact-icon" viewBox="0 0 24 24"><path fill="var(--orange)" d="M6.6 10.8a15.1 15.1 0 0 0 6.6 6.6l2.2-2.2a1 1 0 0 1 1-.25 11.4 11.4 0 0 0 3.6.57 1 1 0 0 1 1 1V20a1 1 0 0 1-1 1A17 17 0 0 1 3 4a1 1 0 0 1 1-1h3.5a1 1 0 0 1 1 1c0 1.25.2 2.45.57 3.57a1 1 0 0 1-.25 1z"/></svg>
        </li>
        <li>daniel@tkvitality.com
          <svg class="contact-icon" viewBox="0 0 24 24"><rect x="2" y="5" width="20" height="14" fill="none" stroke="var(--orange)" stroke-width="2"/><path d="M2 5l10 8 10-8" fill="none" stroke="var(--orange)" stroke-width="2"/></svg>
        </li>
        <li>www.tkvitality.com/my/username
          <svg class="contact-icon" viewBox="0 0 24 24"><g fill="none" stroke="var(--orange)" stroke-width="2"><circle cx="12" cy="12" r="10"/><ellipse cx="12" cy="12" rx="4" ry="10"/><path d="M2 12h20"/></g></svg>
        </li>
      </ul>
    </div>
  </section>

</main>
</body>
</html>
```